Video App Design

Test of Compatibility
We are looking for a creative designer who is capable of designing mobile application in a trendy manner and at the same time taking into consideration User Interface and technical logic.
This simple test of the design will include 4 different pages, that fits together. In addition, the functions of each page should include the logical buttons required (example Back Button).
1st Page: Design a Video page for Mobile Application.
(Imaging a App which only showcase video shared on Plumtree)
This includes the size size of the video (4:3 and/or 16:9)
The Video should be able to play directly off the page.
The Video layout should include:
1) User Profile Picture and Name
2) Video Name
3) Like Counter/Button
4) Share Button
5) A 160 Character description
6) 5 additional generic icons
7) Rating (Optional)
The toolbar should include the following functions:
1) Change categories
2) Filter
3) Search
4) A Slider Button
2nd Page: Design a Profile Page
It should include:
1) Profile Picture
2) Edit Profile
3) Number of followers
4) Videos that were uploaded by user
5) A button to show videos shared by the User
6) A button to show videos Like by the User
7) An Icon to show verified Account
8) Upload video (Optional: If not, where should this be)
2nd Page Part II - Edit Profile
This will include the fields to be included
1) Real Name
2) Display Name
3) Email Address and change email
4) Password and change password
5) A 160 Character description of the User. (with character count)
2nd Page Part III: Add Video Page
It should include:
1) Choosing categories and subcategories
2) Upload Pictures (Preview of final picture to be uploaded)
3) Upload Video
4) Video Name (preview of final video to be uploaded)
5) Video Description (with character counter)
6) A Huge chunk of words (Example:Terms and Condition)
3rd Page: A Pop up of Video Page
This would include
1) Video
2) Pictures added to the Video
1) User Profile Picture
2) A button to follow the user
3) Video Name
4) Like Counter/Button
5) Share Button
6) A 160 Character description
7) 5 additional generic icons
8) Video Description
9) Rating (Optional)
10) Reviews
11) Displaying the huge chunk of words (Example:Terms and Condition)
You can contact me at info@vemarustudio.com for more information.

```html
<!DOCTYPE html>
<html lang="en">
<head>
<meta charset="utf-8">
<title>Video App Design Contest</title>
<link href="https://fonts.googleapis.com/css2?family=Roboto:wght@400;500;700&display=swap" rel="stylesheet">
<style>
:root{
  --stage:#333333;
  --rule:#4a4a4a;
  --teal:#1a8d92;
  --teal-dark:#137579;
  --white:#ffffff;
  --field:#e6e6e6;
  --field-line:#cfcfcf;
  --ink:#333333;
  --muted:#777777;
  --star:#e3a224;
  --red:#d9292b;
}
*{box-sizing:border-box;margin:0;padding:0}
html,body{width:1200px;height:900px;overflow:hidden;background:var(--stage);font-family:'Roboto',Arial,sans-serif;color:var(--ink)}
.canvas{position:relative;width:1200px;height:900px}
.headline{position:absolute;top:60px;left:0;width:1200px;text-align:center;font-size:70px;line-height:80px;font-weight:400;color:var(--white);letter-spacing:0.5px}
.divider{position:absolute;top:207px;left:40px;width:1120px;height:1px;background:var(--rule)}
.screen{position:absolute;top:358px;width:230px;height:410px;background:var(--white);overflow:hidden;border-radius:2px}
.screen--home{left:43px}
.screen--profile{left:334px}
.screen--edit{left:624px}
.screen--upload{left:924px}
.abs{position:absolute}
.status-bar{position:absolute;top:0;left:0;width:100%;height:18px;background:var(--teal-dark);color:var(--white);font-size:9.5px;display:flex;align-items:center;justify-content:space-between;padding:0 5px}
.app-bar{position:absolute;top:18px;left:0;width:100%;height:29px;background:var(--teal);color:var(--white);font-size:14px;font-weight:500;display:flex;align-items:center;justify-content:center}
.app-bar svg{position:absolute;top:7px}
.app-bar .lead{left:8px}
.app-bar .trail{right:9px}
.box{position:absolute;background:var(--field);border:1px solid var(--field-line);font-size:10px;color:var(--ink);display:flex;align-items:center;padding:0 8px}
.teal-label{position:absolute;color:var(--teal);font-size:9.5px}
.small{font-size:6.5px;color:var(--muted)}
.photo{position:absolute}
/* home */
.select-btn{position:absolute;top:52px;height:20px;border:1px solid #8a8a8a;border-radius:2px;background:#f0f0f0;font-size:11px;display:flex;align-items:center;padding:0 4px;gap:4px}
.card{position:absolute;left:10px;top:86px;width:210px;height:198px;background:#f4f4f4;border:1px solid #dddddd}
.avatar{position:absolute;border-radius:50%;background:radial-gradient(circle at 50% 40%,#c9a58a,#5c4636 70%,#2d2b2f)}
.avatar--ring{border:2px solid var(--teal)}
.video-frame{position:absolute;left:11px;top:121px;width:208px;height:138px;background:linear-gradient(135deg,#34379a 0%,#6b5fc2 45%,#1d2a6b 100%)}
.video-controls{position:absolute;left:11px;top:246px;width:208px;height:13px;background:#111;display:flex;align-items:center;padding:0 4px;gap:4px;color:#fff;font-size:7px}
.video-controls .track{flex:1;height:2px;background:#666;position:relative}
.video-controls .track::before{content:"";position:absolute;left:0;top:-2px;width:6px;height:6px;border-radius:50%;background:var(--red)}
.action-row{position:absolute;left:10px;top:262px;width:210px;height:21px;background:#e7e7e7;display:flex;font-size:10px}
.action-row span{flex:1;display:flex;align-items:center;justify-content:center;gap:6px}
.action-row span+span{border-left:1px solid #cfcfcf}
.video-title{position:absolute;left:14px;top:291px;font-size:10px}
.desc-box{position:absolute;left:10px;top:309px;width:210px;height:61px;background:#e9e9e9;border:1px solid #d4d4d4}
.desc-box p{position:absolute;left:4px;top:6px;width:200px;font-size:4.8px;line-height:6px;color:#555}
.desc-box .more{position:absolute;left:0;bottom:0;width:100%;height:14px;border-top:1px solid #c9c9c9;font-size:8px;text-align:center;line-height:13px}
.rating-bar{position:absolute;left:10px;top:378px;width:210px;height:20px;background:#e7e7e7;border:1px solid #d4d4d4;display:flex;align-items:center;justify-content:space-between;padding:0 4px;font-size:10px}
/* profile */
.cover{position:absolute;left:0;top:47px;width:230px;height:138px;background:linear-gradient(90deg,#5a5a5f 0%,#8c8380 45%,#b29c8c 60%,#6e6a6a 100%)}
.icon-action{position:absolute;top:83px;width:60px;text-align:center;color:#fff;font-size:8px}
.icon-action .dot{width:20px;height:20px;border-radius:50%;background:var(--teal);margin:0 auto 3px;display:flex;align-items:center;justify-content:center}
.profile-name{position:absolute;left:0;top:130px;width:230px;text-align:center;color:#fff;font-size:11px;font-weight:700}
.profile-loc{position:absolute;left:0;top:143px;width:230px;text-align:center;color:#fff;font-size:5.5px}
.followers{position:absolute;left:40px;top:156px;width:148px;height:19px;background:#f1f1f1;border:1px solid #ccc;display:flex;align-items:center;padding:0 6px;gap:6px;font-size:9.5px}
.tabs{position:absolute;left:10px;top:190px;width:210px;height:19px;display:flex;font-size:10px;gap:2px}
.tabs span{flex:1;display:flex;align-items:center;justify-content:center;gap:4px;background:#e4e4e4;border:1px solid #d0d0d0}
.tabs .active{background:var(--teal);color:#fff;border-color:var(--teal)}
.list-item{position:absolute;left:6px;width:218px;height:62px;border-bottom:1px solid #e2e2e2}
.list-item .thumb{position:absolute;left:4px;top:0;width:62px;height:47px}
.list-item .t{position:absolute;left:76px;top:1px;font-size:9.5px}
.list-item .m{position:absolute;left:76px;font-size:6.5px;color:#444;display:flex;gap:4px;align-items:center}
</style>
</head>
<body>
<div class="canvas">
  <h1 class="headline">Video App Design Contest</h1>
  <div class="divider"></div>

  <!-- Home screen -->
  <section class="screen screen--home">
    <div class="status-bar"><span>●●●●● NOVA</span><span>✱ 82% ▮</span></div>
    <div class="app-bar">
      <svg class="lead" width="16" height="14" viewBox="0 0 16 14"><path d="M1 2h14M1 7h14M1 12h14" stroke="#fff" stroke-width="2"/></svg>
      Home
      <svg class="trail" width="16" height="16" viewBox="0 0 16 16"><circle cx="6.5" cy="6.5" r="5" fill="none" stroke="#fff" stroke-width="2"/><path d="M10 10l5 5" stroke="#fff" stroke-width="2.2"/></svg>
    </div>
    <div class="select-btn" style="left:17px;width:113px">Change categories
      <svg width="8" height="6" viewBox="0 0 8 6"><path d="M1 1l3 3 3-3" fill="none" stroke="#333" stroke-width="1.3"/></svg></div>
    <div class="select-btn" style="left:150px;width:63px;justify-content:center">
      <svg width="10" height="10" viewBox="0 0 10 10"><path d="M1 1h8L6 5v4L4 8V5z" fill="none" stroke="#333"/></svg>Filter</div>
    <div class="card"></div>
    <div class="avatar" style="left:14px;top:90px;width:28px;height:28px"></div>
    <div class="abs" style="left:50px;top:92px;font-size:10px;color:var(--teal)">Marco Delane</div>
    <div class="abs small" style="left:53px;top:105px;font-size:5.5px">⚲ California, CA</div>
    <svg class="abs" style="left:167px;top:97px" width="14" height="12" viewBox="0 0 14 12"><path d="M7 11.5L1.5 6A3.2 3.2 0 017 1.8 3.2 3.2 0 0112.5 6z" fill="var(--teal)"/></svg>
    <div class="abs" style="left:187px;top:97px;font-size:10px">3250</div>
    <div class="video-frame" role="img" aria-label="Video still of a studio news show with a presenter at a desk"></div>
    <div class="video-controls">
      <svg width="6" height="7" viewBox="0 0 6 7"><path d="M0 0l6 3.5L0 7z" fill="#fff"/></svg>
      <div class="track"></div><span>0:00/3:54</span>
    </div>
    <div class="action-row">
      <span><svg width="14" height="12" viewBox="0 0 14 12"><path d="M7 11L1.5 5.7A3 3 0 017 1.8a3 3 0 015.5 3.9z" fill="none" stroke="var(--teal)" stroke-width="1.3"/></svg>Like</span>
      <span><svg width="12" height="12" viewBox="0 0 12 12"><circle cx="9.5" cy="2.2" r="1.7" fill="none" stroke="var(--teal)"/><circle cx="2.5" cy="6" r="1.7" fill="none" stroke="var(--teal)"/><circle cx="9.5" cy="9.8" r="1.7" fill="none" stroke="var(--teal)"/><path d="M4 5.2l4-2.2M4 6.8l4 2.2" stroke="var(--teal)"/></svg>Share</span>
    </div>
    <div class="video-title">The Open Story - Helena Marsh</div>
    <div class="desc-box">
      <p>A short note about this clip. The host sits down with guests to talk about the day's news and the story behind it, recorded live in the studio and shared for viewers who want the full account of the week ahead.</p>
      <div class="more">See More</div>
    </div>
    <div class="rating-bar"><span>Ratings</span><span style="color:var(--star);font-size:14px;letter-spacing:1px">★★★★☆</span></div>
  </section>

  <!-- Profile screen -->
  <section class="screen screen--profile">
    <div class="status-bar"><span>●●●●● NOVA</span><span>✱ 82% ▮</span></div>
    <div class="app-bar">
      <svg class="lead" width="10" height="14" viewBox="0 0 10 14"><path d="M8 1L2 7l6 6" fill="none" stroke="#fff" stroke-width="2"/></svg>
      Profile
    </div>
    <div class="cover" role="img" aria-label="Blurred cover backdrop in warm grey tones"></div>
    <div class="avatar avatar--ring" style="left:80px;top:55px;width:70px;height:70px" role="img" aria-label="Profile portrait"></div>
    <div class="icon-action" style="left:15px"><div class="dot"><svg width="10" height="10" viewBox="0 0 10 10"><path d="M5 7V1M2 4l3-3 3 3M1 9h8" fill="none" stroke="#fff" stroke-width="1.4"/></svg></div>Upload</div>
    <div class="icon-action" style="left:151px"><div class="dot"><svg width="10" height="10" viewBox="0 0 10 10"><path d="M2 1h4l2 2v6H2z" fill="none" stroke="#fff" stroke-width="1.2"/></svg></div>Edit Profile</div>
    <div class="profile-name">Marco Delane <svg width="9" height="9" viewBox="0 0 10 10"><circle cx="5" cy="5" r="5" fill="var(--teal)"/><path d="M2.7 5l1.6 1.6L7.4 3.5" fill="none" stroke="#fff" stroke-width="1.3"/></svg></div>
    <div class="profile-loc">⚲ California, CA</div>
    <div class="followers">
      <svg width="16" height="10" viewBox="0 0 16 10"><path d="M1 5q7-8 14 0-7 8-14 0z" fill="var(--teal)"/><circle cx="8" cy="5" r="2" fill="#fff"/></svg>
      <span>Followers</span><span style="margin-left:auto">1258</span>
    </div>
    <div class="tabs">
      <span><svg width="10" height="9" viewBox="0 0 10 10"><path d="M5 7V1M2 4l3-3 3 3M1 9h8" fill="none" stroke="var(--teal)" stroke-width="1.5"/></svg>Uploaded</span>
      <span class="active"><svg width="10" height="10" viewBox="0 0 12 12"><circle cx="9.5" cy="2.2" r="1.8" fill="#fff"/><circle cx="2.5" cy="6" r="1.8" fill="#fff"/><circle cx="9.5" cy="9.8" r="1.8" fill="#fff"/><path d="M4 5.2l4-2.2M4 6.8l4 2.2" stroke="#fff"/></svg>Shared</span>
      <span><svg width="11" height="10" viewBox="0 0 14 12"><path d="M7 11.5L1.5 6A3.2 3.2 0 017 1.8 3.2 3.2 0 0112.5 6z" fill="var(--teal)"/></svg>Liked</span>
    </div>
    <div class="list-item" style="top:218px">
      <div class="thumb photo" role="img" aria-label="Football match thumbnail" style="background:linear-gradient(135deg,#3a4f7a,#b23a3a)"></div>
      <div class="t">Top ten goals in history</div>
      <div class="m" style="top:14px">By&nbsp; Football fans club</div>
      <div class="m" style="top:24px">👁 2,558,325 &nbsp;Views</div>
      <div class="m" style="top:33px">♥ 5,581 &nbsp;Likes</div>
    </div>
    <div class="list-item" style="top:280px">
      <div class="thumb photo" role="img" aria-label="Wrestling event thumbnail" style="background:linear-gradient(135deg,#1f2a44,#c06a3a)"></div>
      <div class="t">Ring Clash 29 - Marco</div>
      <div class="m" style="top:14px">By&nbsp; Ring Boss Official</div>
      <div class="m" style="top:24px">👁 2,200,237 &nbsp;Views</div>
      <div class="m" style="top:33px">♥ 7,781 &nbsp;Likes</div>
    </div>
    <div class="list-item" style="top:343px">
      <div class="thumb photo" role="img" aria-label="Anatomy lesson thumbnail" style="background:linear-gradient(135deg,#2a2a3a,#d8643a 60%,#e6b04a)"></div>
      <div class="t">Anatomy Of the Skull</div>
      <div class="m" style="top:14px">By&nbsp; Anatomy Channel</div>
      <div class="m" style="top:24px">👁 218,325 &nbsp;Views</div>
      <div class="m" style="top:33px">♥ 7,781 &nbsp;Likes</div>
    </div>
    <div class="photo" role="img" aria-label="Next video thumbnail" style="left:10px;top:405px;width:62px;height:10px;background:#3b3b48"></div>
  </section>

  <!-- Edit profile screen -->
  <section class="screen screen--edit">
    <div class="status-bar"><span>●●●●● NOVA</span><span>✱ 82% ▮</span></div>
    <div class="app-bar">
      <svg class="lead" width="10" height="14" viewBox="0 0 10 14"><path d="M8 1L2 7l6 6" fill="none" stroke="#fff" stroke-width="2"/></svg>
      Edit profile
      <svg class="trail" width="13" height="13" viewBox="0 0 13 13"><rect x="1" y="1" width="11" height="11" fill="none" stroke="#fff" stroke-width="1.2"/><path d="M3.5 6.5l2 2 4-4.5" fill="none" stroke="#fff" stroke-width="1.3"/></svg>
    </div>
    <div class="avatar avatar--ring" style="left:15px;top:55px;width:73px;height:73px" role="img" aria-label="Profile portrait"></div>
    <div class="teal-label" style="left:95px;top:63px">Display Name</div>
    <div class="box" style="left:92px;top:77px;width:128px;height:18px">Marco Delane<span style="margin-left:auto;color:var(--teal)">✎</span></div>
    <div class="teal-label" style="left:95px;top:99px">Real Name</div>
    <div class="box" style="left:92px;top:113px;width:128px;height:18px">Marcus T Delane<span style="margin-left:auto;color:var(--teal)">✎</span></div>
    <div class="teal-label" style="left:13px;top:145px">Email Adress</div>
    <div class="box" style="left:10px;top:159px;width:210px;height:18px;padding-left:3px">marcodelane@inboxly.com<span style="margin-left:auto;color:var(--teal)">✎</span></div>
    <div class="teal-label" style="left:13px;top:181px">Description</div>
    <div class="box" style="left:10px;top:196px;width:210px;height:59px;align-items:flex-start;padding:4px 3px;font-size:6.5px">Description&nbsp; about you......<span style="margin-left:auto;font-size:5.5px">140/160</span></div>
  </section>

  <!-- Upload screen -->
  <section class="screen screen--upload">
    <div class="status-bar"><span>●●●●● NOVA</span><span>✱ 82% ▮</span></div>
    <div class="app-bar">
      <svg class="lead" width="10" height="14" viewBox="0 0 10 14"><path d="M8 1L2 7l6 6" fill="none" stroke="#fff" stroke-width="2"/></svg>
      Upload Videos
      <svg class="trail" width="14" height="13" viewBox="0 0 14 13"><path d="M7 1v7M3.5 4.5L7 1l3.5 3.5" fill="none" stroke="#fff" stroke-width="1.6"/><path d="M1 8v4h12V8" fill="#fff"/></svg>
    </div>
    <div class="box" style="left:10px;top:67px;width:209px;height:19px">Select Video File<span style="margin-left:auto;color:var(--teal);font-size:8px">Browse</span></div>
    <div class="box" style="left:10px;top:99px;width:209px;height:19px">Video Name</div>
    <div class="box" style="left:10px;top:131px;width:209px;height:19px">Select Categories
      <svg style="margin-left:auto" width="9" height="6" viewBox="0 0 9 6"><path d="M1 1l3.5 3.5L8 1" fill="none" stroke="#333" stroke-width="1.3"/></svg></div>
    <div class="box" style="left:10px;top:164px;width:209px;height:59px;align-items:flex-start;padding:4px 3px;font-size:7.5px">Description&nbsp; about Videos......</div>
    <div class="abs small" style="left:190px;top:225px;font-size:5.5px">140/160</div>
    <div class="box" style="left:10px;top:239px;width:209px;height:58px"></div>
    <div class="photo" role="img" aria-label="Preview image of two smartphones" style="left:17px;top:245px;width:78px;height:46px;background:linear-gradient(135deg,#4a4a4a,#a9a9a9 55%,#5a5a5a)"></div>
    <div class="abs" style="left:106px;top:248px;font-size:9.5px">Select Preview</div>
    <div class="abs" style="left:106px;top:270px;font-size:6.5px">handset.jpeg</div>
  </section>
</div>
</body>
</html>
```